Frostwyn.co - Polar Expeditions Specialists

We need a modern, visually striking business card for Frostwyn.co, a company specialized in selling expedition cruises to the most remote regions on Earth, with a focus on the Arctic and Antarctica. The design should instantly communicate that the cardholder is an expert in polar travel. Use clean, premium aesthetics with cool tones like icy blue and white, possibly incorporating polar imagery (ice, glaciers, penguins, etc.)

Attached the logo

Contact Information for Business Card

Feels high-end and trustworthy.. Visually memorable — encourages people to keep it

Colors
0054AA
0677BA
7BADD7
CADEEF
E8F1F8

Requirements
Must have
• ice, glaciers, penguins, montains
Nice to have
• modern, transparente,

```html
<!DOCTYPE html>
<html lang="en">
<head>
<meta charset="UTF-8">
<title>Frostwyn.co Business Card</title>
<link href="https://fonts.googleapis.com/css2?family=Poppins:wght@400;500;600;700&display=swap" rel="stylesheet">
<style>
  :root {
    --stage: #dfe2e6;
    --card-front: #3b69a6;
    --front-ink: #1f5590;
    --brand-blue: #3474b8;
    --text-dark: #1b1f24;
    --card-white: #ffffff;
    --tint-light: #cadeef;
    --tint-pale: #e8f1f8;
  }
  * { margin: 0; padding: 0; box-sizing: border-box; }
  html, body { width: 900px; height: 1200px; overflow: hidden; }
  body {
    background: var(--stage);
    font-family: "Poppins", sans-serif;
    position: relative;
  }
  .card {
    position: absolute;
    left: 134px;
    width: 633px;
    height: 364px;
    overflow: hidden;
  }
  .card--front { top: 212px; background: var(--card-front); }
  .card--back { top: 624px; background: var(--card-white); }

  .front-mark {
    position: absolute;
    left: 240px; top: 48px;
    width: 152px; height: 132px;
    border-radius: 8px;
    background: linear-gradient(180deg, #3a6aa6, #2e5e98);
  }
  .front-wordmark {
    position: absolute;
    left: 0; right: 0; top: 200px;
    text-align: center;
    font-weight: 700;
    font-size: 68px;
    line-height: 1;
    color: var(--front-ink);
    letter-spacing: 0.5px;
  }
  .front-tagline {
    position: absolute;
    left: 0; right: 0; top: 282px;
    text-align: center;
    font-weight: 600;
    font-size: 21px;
    color: var(--front-ink);
  }

  .back-wordmark {
    position: absolute;
    left: 33px; top: 36px;
    font-weight: 700;
    font-size: 44px;
    line-height: 1.1;
    color: var(--brand-blue);
    white-space: nowrap;
  }
  .back-tagline {
    position: absolute;
    left: 33px; top: 90px;
    font-weight: 600;
    font-size: 16.5px;
    color: var(--brand-blue);
    white-space: nowrap;
  }
  .holder-name {
    position: absolute;
    left: 33px; top: 157px;
    font-weight: 700;
    font-size: 25px;
    color: var(--brand-blue);
  }
  .holder-role {
    position: absolute;
    left: 33px; top: 188px;
    font-weight: 500;
    font-size: 17px;
    letter-spacing: 1px;
    color: var(--text-dark);
  }
  .contact-list {
    position: absolute;
    left: 33px; top: 225px;
    list-style: none;
  }
  .contact-list li {
    display: flex;
    align-items: center;
    height: 25.5px;
    font-size: 15px;
    font-weight: 500;
    color: var(--text-dark);
    letter-spacing: 1px;
  }
  .contact-list li.phone { letter-spacing: 3.4px; }
  .contact-list svg { width: 14px; height: 14px; margin-right: 8px; fill: var(--brand-blue); flex: none; }

  .back-illustration {
    position: absolute;
    left: 345px; top: 36px;
    width: 288px; height: 291px;
    background: linear-gradient(180deg, #3a7bbd 0%, var(--brand-blue) 100%);
    border-radius: 140px 140px 0 0;
  }
</style>
</head>
<body>
  <section class="card card--front">
    <div class="front-mark" role="img" aria-label="Brand symbol area: polar bear with stars"></div>
    <h1 class="front-wordmark">Frostwyn.co</h1>
    <p class="front-tagline">Polar Expeditions Specialists</p>
  </section>

  <section class="card card--back">
    <h2 class="back-wordmark">Frostwyn.co</h2>
    <p class="back-tagline">Polar Expeditions Specialists</p>
    <p class="holder-name">Dalton Reeve</p>
    <p class="holder-role">Owner</p>
    <ul class="contact-list">
      <li class="phone">
        <svg viewBox="0 0 24 24"><path d="M6.6 10.8c1.4 2.8 3.8 5.1 6.6 6.6l2.2-2.2c.3-.3.7-.4 1-.2 1.1.4 2.3.6 3.6.6.6 0 1 .4 1 1V20c0 .6-.4 1-1 1C10.6 21 3 13.4 3 4c0-.6.4-1 1-1h3.5c.6 0 1 .4 1 1 0 1.3.2 2.5.6 3.6.1.3 0 .7-.2 1z"/></svg>
        555-214-7093
      </li>
      <li class="phone">
        <svg viewBox="0 0 24 24"><path d="M7 1h10a2 2 0 0 1 2 2v18a2 2 0 0 1-2 2H7a2 2 0 0 1-2-2V3a2 2 0 0 1 2-2zm0 3v14h10V4zm5 15.5a1 1 0 1 0 0 2 1 1 0 0 0 0-2z"/></svg>
        555-386-1147
      </li>
      <li>
        <svg viewBox="0 0 24 24"><path d="M2 5h20v2l-10 6L2 7zm0 4.3l10 6 10-6V19H2z"/></svg>
        info@Frostwyn.co
      </li>
      <li>
        <svg viewBox="0 0 24 24"><path d="M12 2a10 10 0 1 0 0 20 10 10 0 0 0 0-20zm6.9 6h-3a15 15 0 0 0-1.3-3.9A8 8 0 0 1 18.9 8zM12 4c.8 1.2 1.5 2.5 1.9 4h-3.8c.4-1.5 1.1-2.8 1.9-4zM4.3 14a8 8 0 0 1 0-4h3.4a16 16 0 0 0 0 4zm.8 2h3a15 15 0 0 0 1.3 3.9A8 8 0 0 1 5.1 16zM8.1 8h-3a8 8 0 0 1 4.3-3.9C8.9 5.3 8.4 6.6 8.1 8zM12 20c-.8-1.2-1.5-2.5-1.9-4h3.8c-.4 1.5-1.1 2.800-1.9 4zm2.3-6H9.7a14 14 0 0 1 0-4h4.6a14 14 0 0 1 0 4zm.3 5.9c.6-1.2 1-2.5 1.3-3.9h3a8 8 0 0 1-4.3 3.9zm1.7-5.9a16 16 0 0 0 0-4h3.4a8 8 0 0 1 0 4z"/></svg>
        Frostwyn.co
      </li>
    </ul>
    <div class="back-illustration" role="img" aria-label="Large brand symbol: polar bear with two penguins and stars on ice"></div>
  </section>
</body>
</html>
```